Professional and creative business card design for recruiting service providers

Our company supports German medium-sized companies in filling vacancies promptly. For this we use social media marketing and bring our customers into the visibility.

We want a professional but also creative design for our business cards.

Please look at halvenrick-consult.de to get an impression of our CI.

Target Market(s)

Small and medium-sized companies in Germany from the industry

Industry/Entity Type

Industrie, Handwerk

Contact Information for Business Card

Name, Position, Telefonnummer, Email, Website

Colors
EE7325
F08F49
F5BC92
FAE3D3
FDF4ED

Requirements
Must have
• A picture of the employee and in the style of www.halvenrick-consult.de

```html
<!DOCTYPE html>
<html lang="de">
<head>
<meta charset="utf-8">
<title>Halvenrick Consult – Visitenkarte</title>
<link rel="stylesheet" href="https://fonts.googleapis.com/css2?family=Lato:wght@400;700;900&display=swap">
<style>
  :root {
    --orange: #ee7325;
    --orange-soft: #f08f49;
    --paper: #f1f1f1;
    --ink: #1c1c1c;
    --black: #0d0d0d;
    --stage: #d9d9d9;
  }
  * { box-sizing: border-box; margin: 0; padding: 0; }
  html, body { width: 1200px; height: 873px; overflow: hidden; }
  body {
    background: var(--stage);
    font-family: "Lato", Arial, sans-serif;
    color: var(--ink);
    display: flex;
    align-items: center;
    justify-content: center;
    gap: 44px;
  }
  .card {
    position: relative;
    width: 540px;
    height: 308px;
    overflow: hidden;
    box-shadow: 0 6px 18px rgba(0,0,0,.18);
  }

  /* front */
  .card-front { background: var(--paper); }
  .employee-photo {
    position: absolute;
    right: 0; top: 30px;
    width: 250px; height: 278px;
    background: linear-gradient(180deg, #e9e5e1 0%, #c9b8a8 38%, #3a3a3e 62%, #2b2b2f 100%);
  }
  .brand {
    position: absolute;
    left: 48px; top: 38px;
    display: flex; align-items: center; gap: 10px;
  }
  .brand-mark { width: 34px; height: 34px; background: var(--orange); }
  .brand-name {
    font-weight: 700;
    font-size: 19px;
    line-height: 22px;
    letter-spacing: 1.5px;
    text-transform: uppercase;
    color: var(--ink);
  }
  .person { position: absolute; left: 48px; top: 124px; }
  .person-name {
    color: var(--orange);
    font-weight: 900;
    font-size: 15px;
    text-transform: uppercase;
  }
  .person-role { font-size: 11px; margin-top: 2px; }
  .contacts { list-style: none; margin-top: 14px; font-size: 11px; }
  .contacts li { display: flex; align-items: center; gap: 7px; line-height: 16px; }
  .contacts svg { width: 9px; height: 9px; fill: var(--orange); }
  .address-band {
    position: absolute;
    left: 0; right: 0; top: 240px;
    height: 46px;
    background: rgba(238,115,37,.93);
    display: flex; align-items: center;
    padding-left: 48px;
    font-size: 10.5px;
    color: var(--ink);
  }

  /* back */
  .card-back {
    background: radial-gradient(circle at 50% 50%, #1e1e1e 0%, var(--black) 75%);
    display: flex; flex-direction: column;
    align-items: center; justify-content: center;
  }
  .back-pattern {
    position: absolute; inset: 0;
    background: linear-gradient(135deg, rgba(60,60,60,.35), rgba(20,20,20,.1));
  }
  .card-back .brand { position: relative; left: auto; top: auto; gap: 14px; }
  .card-back .brand-mark { width: 52px; height: 52px; }
  .card-back .brand-name { color: #fff; font-size: 28px; line-height: 32px; letter-spacing: 2px; }
  .web {
    position: relative;
    margin-top: 34px;
    font-size: 10.5px;
    color: #fff;
  }
  .web span { color: var(--orange-soft); }
</style>
</head>
<body>
  <section class="card card-front">
    <div class="employee-photo" role="img" aria-label="Porträtfoto des Mitarbeiters im dunklen Sakko"></div>
    <div class="brand">
      <div class="brand-mark"></div>
      <div class="brand-name">Halvenrick<br>Consult</div>
    </div>
    <div class="person">
      <div class="person-name">Jonas Brendel</div>
      <div class="person-role">Senior Recruiting Consultant</div>
      <ul class="contacts">
        <li><svg viewBox="0 0 10 10"><path d="M2 0 L4 2.5 L3 3.6 Q4.5 6 6.4 7 L7.5 6 L10 8 L8.6 10 Q3 9 0 1.4 Z"/></svg>0172 394 2716</li>
        <li><svg viewBox="0 0 10 10"><path d="M0 2 H10 V8.5 H0 Z M0.6 2.4 L5 5.8 L9.4 2.4" stroke="#f1f1f1" stroke-width=".8"/></svg>info@halvenrick-consult.de</li>
        <li><svg viewBox="0 0 10 10"><circle cx="5" cy="5" r="5"/><path d="M0 5 H10 M5 0 V10" stroke="#f1f1f1" stroke-width=".7"/></svg>www.halvenrick-consult.de</li>
      </ul>
    </div>
    <div class="address-band">Halvenrick Consult GmbH, Lindenhofer Strasse 42b, 70182 Stuttgart</div>
  </section>

  <section class="card card-back">
    <div class="back-pattern" role="img" aria-label="Dezentes dunkles Hintergrundmuster"></div>
    <div class="brand">
      <div class="brand-mark"></div>
      <div class="brand-name">Halvenrick<br>Consult</div>
    </div>
    <div class="web">www.<span>halvenrick-consult</span>.de</div>
  </section>
</body>
</html>
```